Cosmetic Dentist Practice needs stationery package/logo

I need a letterhead, envelope and business card for a cosmetic and Dental Inplant practice in an upscale part of Houston. The business card will be a size 3.5 x 2 and the letterhead will be 8.5" x 11" with a standard #10 envelope.
I have uploaded a file with an idea that the dentist had for his cards. Please note that this is not the size that the card should be. It does provide the information required.
Thank you all for your submissions. They were each unique and special in their own way. My client has made a selection that he feels best meets his needs. I appreciate each of you taking the time to offer designs. Good luck to each of you...I hope to see you back in Sketchforum on future projects.

```html
<!DOCTYPE html>
<html lang="en">
<head>
<meta charset="utf-8">
<title>Larkspur Dental Studio — Letterhead</title>
<link href="https://fonts.googleapis.com/css2?family=Questrial&display=swap" rel="stylesheet">
<style>
  :root {
    --backdrop: #e4e5e6;
    --paper: #f7f7f7;
    --brand-blue: #4f87a6;
    --ink-grey: #5c6166;
    --ink-soft: #80868b;
    --shadow: rgba(0, 0, 0, 0.12);
  }
  html, body {
    margin: 0;
    padding: 0;
    width: 1200px;
    height: 936px;
    overflow: hidden;
    background: var(--backdrop);
  }
  .canvas {
    width: 1200px;
    height: 936px;
    display: flex;
    align-items: center;
    justify-content: center;
  }
  .letterhead {
    position: relative;
    width: 680px;
    height: 880px;
    background: var(--paper);
    box-shadow: 0 4px 18px var(--shadow);
    overflow: hidden;
  }
  .letterhead__band {
    position: absolute;
    top: 0;
    left: 0;
    right: 0;
    height: 8px;
    background: var(--brand-blue);
  }
  .brand {
    position: absolute;
    top: 62px;
    left: 48px;
    display: flex;
    align-items: center;
    gap: 10px;
  }
  .brand__square {
    width: 10px;
    height: 10px;
    background: var(--brand-blue);
  }
  .brand__name {
    margin: 0;
    font-family: "Questrial", sans-serif;
    font-weight: 400;
    font-size: 19px;
    letter-spacing: 0.3px;
    color: var(--ink-grey);
    line-height: 1;
  }
  .contact {
    position: absolute;
    right: 48px;
    bottom: 44px;
    font-family: "Questrial", sans-serif;
    font-size: 10px;
    line-height: 1.55;
    color: var(--ink-soft);
    text-align: left;
  }
  .contact__label {
    color: var(--brand-blue);
    font-weight: 700;
  }
</style>
</head>
<body>
  <main class="canvas">
    <article class="letterhead">
      <div class="letterhead__band"></div>

      <header class="brand">
        <span class="brand__square" aria-hidden="true"></span>
        <h1 class="brand__name">Larkspur Dental Studio</h1>
      </header>

      <footer class="contact">
        <div class="contact__address">18 Linden Grove Suite 240 E, Houston, TX 77019</div>
        <div class="contact__lines">
          <span class="contact__label">T:</span> 713-555-0142
          <span class="contact__label">F:</span> 713-555-0187
          <span class="contact__label">E:</span> hello@larkspurdental.com
        </div>
      </footer>
    </article>
  </main>
</body>
</html>
```